Software company stationery project
VOLTA Systems business cards, letterhead, stationery
Software company stationery project -
Creative Brief
Professional
Marcus Hale
President
217 Orchard Lane Tuckahoe, NY 10725
(855) 294-5688
marcus.hale@voltasystems.example
www.voltasystems.example
Open to 2 sided or 1, and to your recommended font. Current website is under total reconstruction but the content will be similar. Would like to see if phrase could be used on card - "evidence and property specialists". Software is for police dept's. evidence/property rooms, and tracking those items.

```html
<!DOCTYPE html>
<html lang="en">
<head>
<meta charset="utf-8">
<title>VOLTA Systems Stationery</title>
<link rel="stylesheet" href="https://fonts.googleapis.com/css2?family=Montserrat:wght@400;700&display=swap">
<style>
  :root{
    --backdrop:#e8e3de;
    --paper:#ffffff;
    --ink:#2b2b2b;
    --ink-soft:#6b6b6b;
    --brand-red:#b8362a;
    --brand-dark:#2a1512;
    --print-tint:#ecdcdc;
    --fold:#d8d4d0;
  }
  *{box-sizing:border-box;margin:0;padding:0}
  html,body{width:1200px;height:751px;overflow:hidden}
  body{background:var(--backdrop);font-family:"Montserrat",sans-serif;color:var(--ink);position:relative}
  .sheet{position:absolute;background:var(--paper);box-shadow:0 2px 6px rgba(0,0,0,.25);overflow:hidden}
  .brand{font-family:"Montserrat",sans-serif;font-weight:700;color:var(--brand-dark);line-height:1;white-space:nowrap;display:flex;align-items:center;gap:4px}
  .brand-dot{display:inline-block;background:var(--brand-red);border-radius:50%}
  .contact{font-size:5px;line-height:1.45;color:var(--ink-soft);white-space:nowrap}
  .contact b{color:var(--brand-red);font-weight:700}
  .header{position:absolute;display:flex;align-items:center;gap:10px}
  .swoosh{position:absolute;left:0;width:100%;display:block}
  .fingerprint{position:absolute;border-radius:50% 50% 46% 46%;background:radial-gradient(ellipse at center,var(--print-tint) 0%,rgba(236,220,220,.5) 55%,rgba(255,255,255,0) 72%)}
  .flip{transform:rotate(180deg)}
  .flap-brand{position:absolute;left:0;right:0;display:flex;justify-content:center}
  .person{font-size:6px;font-weight:700;color:var(--brand-red)}
  .person small{display:block;font-size:4.5px;font-weight:400;color:var(--ink-soft)}
  .tagline{font-size:4.5px;color:var(--ink-soft);letter-spacing:.2px}
</style>
</head>
<body>

<svg width="0" height="0" style="position:absolute" aria-hidden="true">
  <defs>
    <linearGradient id="dark-band" x1="0" x2="1" y1="0" y2="0">
      <stop offset="0" stop-color="#2a1512" stop-opacity=".15"/>
      <stop offset=".6" stop-color="#2a1512"/>
      <stop offset="1" stop-color="#1a0c0a"/>
    </linearGradient>
    <linearGradient id="red-band" x1="0" x2="1" y1="0" y2="0">
      <stop offset="0" stop-color="#b8362a" stop-opacity=".1"/>
      <stop offset=".5" stop-color="#b8362a"/>
      <stop offset="1" stop-color="#8d2219"/>
    </linearGradient>
    <symbol id="swoosh-bottom" viewBox="0 0 340 60" preserveAspectRatio="none">
      <path d="M0 60 C120 54 230 32 340 8 L340 24 C230 42 120 58 0 60Z" fill="url(#red-band)"/>
      <path d="M0 60 C140 56 250 38 340 22 L340 60Z" fill="url(#dark-band)"/>
      <path d="M0 60 C150 58 250 46 340 36" stroke="#fff" stroke-width="1.2" fill="none" opacity=".8"/>
    </symbol>
    <symbol id="swoosh-top" viewBox="0 0 340 60" preserveAspectRatio="none">
      <path d="M0 0 L340 0 L340 36 C250 14 140 4 0 0Z" fill="url(#dark-band)"/>
      <path d="M60 0 C170 8 260 26 340 46 L340 36 C260 16 170 4 60 0Z" fill="url(#red-band)"/>
    </symbol>
  </defs>
</svg>

<!-- Letterhead, bottom swoosh -->
<section class="sheet letterhead" style="left:72px;top:36px;width:336px;height:444px">
  <div class="header" style="left:20px;top:24px">
    <div class="brand" style="font-size:13px"><span class="brand-dot" style="width:6px;height:6px"></span>VOLTA Systems</div>
    <div class="contact"><b>Marcus Hale</b> President<br>217 Orchard Lane Tuckahoe, NY 10725<br>(855) 294-5688<br>marcus.hale@voltasystems.example<br>www.voltasystems.example</div>
  </div>
  <div class="fingerprint" role="img" aria-label="Faint fingerprint watermark" style="left:108px;top:168px;width:118px;height:150px"></div>
  <svg class="swoosh" style="bottom:0;height:70px"><use href="#swoosh-bottom"/></svg>
</section>

<!-- Letterhead, top swoosh -->
<section class="sheet letterhead" style="left:432px;top:36px;width:348px;height:456px">
  <svg class="swoosh" style="top:0;height:50px"><use href="#swoosh-top"/></svg>
  <div class="header" style="left:18px;top:40px">
    <div class="brand" style="font-size:13px"><span class="brand-dot" style="width:6px;height:6px"></span>VOLTA Systems</div>
    <div class="contact"><b>Marcus Hale</b> President<br>217 Orchard Lane Tuckahoe, NY 10725<br>(855) 294-5688<br>marcus.hale@voltasystems.example<br>www.voltasystems.example</div>
  </div>
  <div class="fingerprint" role="img" aria-label="Pale red fingerprint watermark" style="left:112px;top:230px;width:124px;height:160px"></div>
</section>

<!-- Envelope, back with flap -->
<section class="sheet envelope" style="left:792px;top:43px;width:367px;height:173px">
  <svg style="position:absolute;left:0;top:0;width:100%;height:40px" viewBox="0 0 367 40" preserveAspectRatio="none" aria-hidden="true">
    <path d="M0 0 L183 38 L367 0" stroke="var(--fold)" fill="none"/>
  </svg>
  <div class="flap-brand" style="top:8px"><div class="brand flip" style="font-size:12px"><span class="brand-dot" style="width:5px;height:5px"></span>VOLTA Systems</div></div>
</section>

<!-- Envelope, front with flap -->
<section class="sheet envelope" style="left:792px;top:233px;width:367px;height:211px">
  <svg style="position:absolute;left:0;top:0;width:100%;height:40px" viewBox="0 0 367 40" preserveAspectRatio="none" aria-hidden="true">
    <path d="M0 0 L183 36 L367 0" stroke="var(--fold)" fill="none"/>
  </svg>
  <div class="flap-brand" style="top:10px"><div class="brand flip" style="font-size:12px"><span class="brand-dot" style="width:5px;height:5px"></span>VOLTA Systems</div></div>
  <div class="header" style="left:16px;top:92px">
    <div class="brand" style="font-size:12px"><span class="brand-dot" style="width:5px;height:5px"></span>VOLTA Systems</div>
    <div class="contact">217 Orchard Lane Tuckahoe, NY 10725<br>(855) 294-5688<br>www.voltasystems.example</div>
  </div>
  <svg class="swoosh" style="bottom:0;height:62px"><use href="#swoosh-bottom"/></svg>
</section>

<!-- Envelope, large -->
<section class="sheet envelope" style="left:792px;top:473px;width:367px;height:259px">
  <div class="header" style="left:14px;top:22px">
    <div class="brand" style="font-size:13px"><span class="brand-dot" style="width:6px;height:6px"></span>VOLTA Systems</div>
    <div class="contact">217 Orchard Lane Tuckahoe, NY 10725<br>(855) 294-5688<br>marcus.hale@voltasystems.example<br>www.voltasystems.example</div>
  </div>
  <svg class="swoosh" style="bottom:0;height:70px"><use href="#swoosh-bottom"/></svg>
</section>

<!-- Envelope, bottom middle -->
<section class="sheet envelope" style="left:408px;top:511px;width:365px;height:221px">
  <svg style="position:absolute;left:0;top:0;width:100%;height:50px" viewBox="0 0 365 50" preserveAspectRatio="none" aria-hidden="true">
    <path d="M0 0 L182 46 L365 0" stroke="var(--fold)" fill="none"/>
  </svg>
  <div class="flap-brand" style="top:14px"><div class="brand flip" style="font-size:12px"><span class="brand-dot" style="width:5px;height:5px"></span>VOLTA Systems</div></div>
  <div class="header" style="left:14px;top:80px">
    <div class="brand" style="font-size:12px"><span class="brand-dot" style="width:5px;height:5px"></span>VOLTA Systems</div>
    <div class="contact">217 Orchard Lane Tuckahoe, NY 10725<br>(855) 294-5688<br>www.voltasystems.example</div>
  </div>
  <svg class="swoosh" style="bottom:0;height:60px"><use href="#swoosh-bottom"/></svg>
</section>

<!-- Business card front -->
<section class="sheet card" style="left:79px;top:523px;width:144px;height:72px">
  <div class="person" style="position:absolute;left:8px;top:10px">Marcus Hale<small>President</small></div>
  <div class="brand" style="position:absolute;right:8px;top:10px;font-size:8px"><span class="brand-dot" style="width:4px;height:4px"></span>VOLTA Systems</div>
  <div class="contact" style="position:absolute;left:8px;top:30px;font-size:4px">217 Orchard Lane Tuckahoe, NY 10725<br>(855) 294-5688<br>marcus.hale@voltasystems.example</div>
  <svg class="swoosh" style="bottom:0;height:18px"><use href="#swoosh-bottom"/></svg>
</section>

<!-- Business card, second variant -->
<section class="sheet card" style="left:238px;top:523px;width:146px;height:72px">
  <svg class="swoosh" style="top:0;height:14px"><use href="#swoosh-top"/></svg>
  <div class="brand" style="position:absolute;left:8px;top:18px;font-size:8px"><span class="brand-dot" style="width:4px;height:4px"></span>VOLTA Systems</div>
  <div class="contact" style="position:absolute;left:8px;top:32px;font-size:4px"><b>Marcus Hale</b> President<br>(855) 294-5688<br>www.voltasystems.example</div>
</section>

<!-- Business card back -->
<section class="sheet card" style="left:238px;top:617px;width:146px;height:81px">
  <div class="flap-brand" style="top:26px"><div class="brand" style="font-size:8px"><span class="brand-dot" style="width:4px;height:4px"></span>VOLTA Systems</div></div>
  <div class="tagline" style="position:absolute;left:0;right:0;top:40px;text-align:center">evidence and property specialists</div>
  <svg class="swoosh" style="bottom:0;height:16px"><use href="#swoosh-bottom"/></svg>
</section>

</body>
</html>
```